Company website for an international IT business

We require a website for our business, Korvel Solutions. The business has two primary areas: Futures, which includes two machine learning/deep learning based products and IT consultancy, which is the service we provide to other businesses.

We bridge cutting-edge research to market.

STYLING:
The site can be on single page or multi-page. This is fully open to suggestion. So long as the look and feel are consistent. Currently, we have no strong preference for colors, styles or layouts.
You can find the logo of our website in the attachment “Korvel-logo.png” and “Korvel-logo-landscape.png”.

CONTENT:
You can find the text of the website in “Website-Content.pdf”, which explains the services and products of our business. The format of the text is also open to suggestion - including breaking up the text into visually appealing sections.
We would also like to include suitable images on the website so that it does not appear to be a text-heavy page. We are happy to have placeholder images on stock image sites if needed. We are open to suggestions on placing of images

Industry/Entity Type

It Company

Coding

Coded - Design and coding required

Number of Pages Required

1 page

Colors

Designer to choose colors to be used in the design.

Requirements
Must have
• A full description of the requirement is in the attachment "Website-Content.pdf"
• The design must have HTML/CSS, and all resources relevant (images, fonts etc)
• We are
Nice to have
• We are open to suggestions on top of the requirement, please reach out and communicate.

```html
<!DOCTYPE html>
<html lang="en">
<head>
<meta charset="utf-8">
<title>Korvel Solutions</title>
<link href="https://fonts.googleapis.com/css2?family=Montserrat:wght@400;600;700;800&family=Open+Sans:wght@400;600&family=Orbitron:wght@700;900&display=swap" rel="stylesheet">
<style>
:root{
  --blue:#1c8fd6;
  --blue-dark:#136ea8;
  --ink:#1d1d1d;
  --text:#6b6b6b;
  --muted:#9a9a9a;
  --dark:#202428;
  --white:#ffffff;
  --light:#f1f2f3;
}
*{box-sizing:border-box;margin:0;padding:0}
html,body{width:1200px;height:4008px;overflow:hidden}
body{font-family:"Open Sans",sans-serif;color:var(--text);background:var(--white);font-size:15px;line-height:1.6}
h1,h2,h3{font-family:"Montserrat",sans-serif}
.section{position:relative;width:1200px;overflow:hidden}
.photo{position:absolute}

/* header */
.site-header{height:128px;display:flex;align-items:center;justify-content:space-between;padding:0 60px 0 70px}
.brand{display:flex;align-items:center;gap:14px;font-family:"Montserrat",sans-serif;font-weight:700;font-size:26px;color:var(--ink);letter-spacing:1px}
.brand-dot{width:64px;height:64px;border-radius:50%;background:var(--blue)}
.header-right{display:flex;flex-direction:column;align-items:flex-end;gap:14px}
.top-contacts{display:flex;gap:26px;font-size:13px;color:var(--muted)}
.top-contacts span{display:flex;align-items:center;gap:8px}
.nav{display:flex;gap:6px;font-family:"Montserrat",sans-serif;font-size:14px}
.nav a{padding:8px 20px;color:var(--muted);text-decoration:none}
.nav a.active{color:var(--blue);border-bottom:3px solid var(--blue)}

/* hero */
.hero{height:552px;background:linear-gradient(180deg,#3c4553 0%,#1f2630 55%,#4a3a2a 100%);text-align:center;color:var(--white)}
.hero .photo{inset:0;background:linear-gradient(180deg,rgba(80,95,115,.5),rgba(20,24,30,.3) 60%,rgba(150,110,60,.35))}
.hero-inner{position:relative;padding-top:190px}
.hero h1{font-size:58px;font-weight:800;letter-spacing:2px}
.hero h2{color:var(--blue);font-size:26px;font-weight:600;margin:4px 0 14px}
.hero p{width:760px;margin:0 auto;font-size:15px;color:#e6e6e6}
.hero-arrow{position:absolute;top:250px;width:30px;height:40px}
.hero-arrow.left{left:20px}.hero-arrow.right{right:20px}

/* welcome */
.welcome{height:448px;text-align:center;padding-top:68px}
.section-title{font-size:42px;font-weight:800;color:var(--ink);letter-spacing:2px}
.section-title em{font-style:normal;color:var(--blue)}
.divider{width:120px;height:14px;margin:8px auto 12px;display:block}
.welcome .lead{width:900px;margin:0 auto;font-size:14px;color:var(--muted)}
.features{display:flex;justify-content:space-between;padding:36px 90px 0}
.feature{width:300px}
.feature svg{width:56px;height:56px}
.feature h3{color:var(--blue);font-size:21px;font-weight:600;margin:6px 0 4px}
.feature p{font-size:14px;color:var(--muted)}

/* futures + consultancy */
.duo{height:432px}
.futures-photo{left:0;top:0;width:600px;height:432px;background:linear-gradient(135deg,#2c3036,#6a6e73)}
.consult-photo{left:600px;top:0;width:600px;height:432px;background:linear-gradient(135deg,#dfe6ec,#8fa6bb 60%,#2f5f8f)}
.futures-text{position:absolute;left:130px;top:96px;width:370px;color:var(--white)}
.futures-text h2{font-size:32px;font-weight:700;letter-spacing:2px;margin-bottom:14px}
.futures-text p{font-size:14px;color:#dcdcdc}
.consult-label{position:absolute;right:40px;bottom:26px;font-family:"Montserrat",sans-serif;font-weight:700;font-size:26px;color:var(--white);letter-spacing:2px;background:rgba(20,24,30,.75);padding:4px 14px}

/* products */
.vigil{height:360px}
.pricewise{height:440px}
.product-photo{top:0;width:600px;height:100%}
.vigil .product-photo{left:0;background:linear-gradient(120deg,#f3f3f3,#9a9a9a 55%,#2c2c2c)}
.pricewise .product-photo{right:0;background:linear-gradient(240deg,#1a1a1a,#7b7b7b 50%,#e9e9e9)}
.product-text{position:absolute;width:500px}
.vigil .product-text{left:660px;top:40px}
.pricewise .product-text{left:70px;top:72px}
.product-text h2{font-family:"Orbitron",sans-serif;font-weight:900;font-size:38px;color:var(--blue-dark);letter-spacing:3px;margin-bottom:12px}
.product-text p{font-size:13px;color:var(--text);margin-bottom:12px}

/* expertise */
.expertise{height:340px;text-align:center;color:var(--white)}
.expertise .photo{inset:0;background:linear-gradient(180deg,#2a2d33,#15181c 60%,#3b3f45)}
.expertise-inner{position:relative;padding-top:92px}
.expertise h2{font-size:42px;font-weight:700;letter-spacing:3px}
.expertise p{width:760px;margin:10px auto 0;font-size:17px;color:#d8d8d8}

/* help */
.help{height:540px;background:linear-gradient(180deg,#fff,#f2f4f6)}
.help h2{position:absolute;left:60px;top:40px;font-size:42px;font-weight:800;color:var(--ink);letter-spacing:1px}
.help-list{position:absolute;left:100px;top:120px;width:560px}
.help-item{display:flex;gap:22px;align-items:flex-start;margin-bottom:44px}
.help-icon{flex:none;width:72px;height:72px;border-radius:50%;background:var(--dark);display:flex;align-items:center;justify-content:center}
.help-item h3{font-family:"Open Sans",sans-serif;font-weight:400;font-size:22px;color:var(--ink);line-height:1.35}
.help-item p{font-size:13px;color:var(--muted)}
.help-photo{left:700px;top:0;width:500px;height:540px;background:linear-gradient(160deg,#f4f6f8 0%,#dbe7f1 35%,#8fb8d9 55%,#2b3440 78%,#12161c 100%)}

/* contact */
.contact{height:500px;color:var(--white)}
.contact .photo{inset:0;background:linear-gradient(180deg,#3a3e44,#1c1f23)}
.contact-inner{position:relative;padding:72px 200px 0;text-align:center}
.contact h2{font-size:42px;font-weight:700;letter-spacing:3px}
.contact .intro{font-size:13px;color:#dcdcdc;margin:8px 0 26px}
.form{display:grid;grid-template-columns:240px 1fr;gap:16px;text-align:left}
.fields{display:flex;flex-direction:column;gap:16px}
.field{height:52px;background:var(--white);color:var(--muted);font-size:13px;padding:14px 16px}
.message{height:188px}
.submit{grid-column:1/3;height:44px;border:2px solid var(--white);text-align:center;font-family:"Montserrat",sans-serif;font-weight:600;font-size:16px;letter-spacing:2px;line-height:40px}

/* footer */
.site-footer{height:268px;background:var(--light);display:flex;justify-content:space-between;padding:40px 70px 0}
.footer-col h3{font-family:"Montserrat",sans-serif;color:var(--blue);font-size:22px;font-weight:700;letter-spacing:1px;margin-bottom:14px}
.post{display:flex;gap:14px;margin-bottom:16px;width:290px}
.post-thumb{flex:none;width:80px;height:56px;background:linear-gradient(135deg,#8a7a6a,#3a3a3a)}
.post p{font-size:12px;color:var(--text);line-height:1.4}
.post span{font-size:11px;color:var(--blue)}
.footer-brand{text-align:center;padding-top:8px}
.footer-brand .brand{flex-direction:column;gap:8px}
.footer-brand .brand-dot{width:96px;height:96px}
.footer-brand small{display:block;margin-top:18px;font-size:12px;color:var(--muted)}
.info{width:290px}
.info li{list-style:none;display:flex;gap:12px;font-size:12px;color:var(--text);margin-bottom:12px;align-items:flex-start}
.info svg{flex:none;width:16px;height:16px}
</style>
</head>
<body>

<header class="section site-header">
  <div class="brand"><span class="brand-dot"></span>KORVEL</div>
  <div class="header-right">
    <div class="top-contacts">
      <span><svg width="14" height="14" viewBox="0 0 24 24"><path fill="#1c8fd6" d="M6.6 10.8a15 15 0 0 0 6.6 6.6l2.2-2.2c.3-.3.7-.4 1-.2 1.1.4 2.3.6 3.6.6.6 0 1 .4 1 1V20c0 .6-.4 1-1 1A17 17 0 0 1 3 4c0-.6.4-1 1-1h3.5c.6 0 1 .4 1 1 0 1.3.2 2.5.6 3.6.1.3 0 .7-.2 1z"/></svg>+61 400 555 010</span>
      <span><svg width="14" height="14" viewBox="0 0 24 24"><path fill="#1c8fd6" d="M2 5h20v14H2zm2 2v.5l8 5 8-5V7z"/></svg>hello@korvel.example</span>
    </div>
    <nav class="nav">
      <a class="active" href="#">Home</a><a href="#">About Us</a><a href="#">Futures</a><a href="#">Consultancy</a><a href="#">News</a><a href="#">Contact Us</a>
    </nav>
  </div>
</header>

<section class="section hero">
  <div class="photo" role="img" aria-label="City skyline at dusk"></div>
  <svg class="hero-arrow left" viewBox="0 0 30 40"><path d="M22 4 8 20l14 16" fill="none" stroke="#fff" stroke-width="3"/></svg>
  <svg class="hero-arrow right" viewBox="0 0 30 40"><path d="M8 4l14 16L8 36" fill="none" stroke="#fff" stroke-width="3"/></svg>
  <div class="hero-inner">
    <h1>KORVEL SOLUTIONS</h1>
    <h2>Business Coaching &amp; Consulting For IT</h2>
    <p>We bridge cutting-edge research to market, turning machine learning and deep learning work into dependable products and practical advice for businesses around the world.</p>
  </div>
</section>

<section class="section welcome">
  <h2 class="section-title">WELCOME TO <em>KORVEL</em></h2>
  <svg class="divider" viewBox="0 0 120 14"><line x1="0" y1="7" x2="50" y2="7" stroke="#ccc"/><circle cx="60" cy="7" r="6" fill="#9a9a9a"/><line x1="70" y1="7" x2="120" y2="7" stroke="#ccc"/></svg>
  <p class="lead">Korvel is an international IT business with two areas of work: Futures, where we build products on machine learning and deep learning research, and IT consultancy, the service we provide to other businesses. Our team brings research results into real use, with clear plans, careful engineering and honest advice at every step of the way.</p>
  <div class="features">
    <div class="feature">
      <svg viewBox="0 0 56 56"><rect x="6" y="10" width="44" height="34" rx="3" fill="none" stroke="#1d1d1d" stroke-width="2.5"/><path d="M22 21l-6 6 6 6M34 21l6 6-6 6M30 18l-4 18" fill="none" stroke="#1c8fd6" stroke-width="2.5"/></svg>
      <h3>Software Development</h3>
      <p>Custom software built with care, tested well and ready for everyday use.</p>
    </div>
    <div class="feature">
      <svg viewBox="0 0 56 56"><circle cx="28" cy="28" r="7" fill="#1c8fd6"/><g stroke="#1d1d1d" stroke-width="2"><line x1="28" y1="21" x2="28" y2="8"/><line x1="28" y1="35" x2="28" y2="48"/><line x1="21" y1="28" x2="8" y2="28"/><line x1="35" y1="28" x2="48" y2="28"/></g><g fill="#1d1d1d"><circle cx="28" cy="6" r="4"/><circle cx="28" cy="50" r="4"/><circle cx="6" cy="28" r="4"/><circle cx="50" cy="28" r="4"/></g></svg>
      <h3>IOT System Design</h3>
      <p>Connected device systems planned from sensor to cloud dashboard.</p>
    </div>
    <div class="feature">
      <svg viewBox="0 0 56 56"><circle cx="28" cy="28" r="10" fill="none" stroke="#1c8fd6" stroke-width="3"/><g stroke="#1d1d1d" stroke-width="4" stroke-linecap="round"><line x1="28" y1="8" x2="28" y2="13"/><line x1="28" y1="43" x2="28" y2="48"/><line x1="8" y1="28" x2="13" y2="28"/><line x1="43" y1="28" x2="48" y2="28"/><line x1="14" y1="14" x2="18" y2="18"/><line x1="38" y1="38" x2="42" y2="42"/><line x1="42" y1="14" x2="38" y2="18"/><line x1="18" y1="38" x2="14" y2="42"/></g></svg>
      <h3>Machine learning solutions</h3>
      <p>Models trained on your data to solve problems that matter to you.</p>
    </div>
  </div>
</section>

<section class="section duo">
  <div class="photo futures-photo" role="img" aria-label="Hands typing on a laptop in low light"></div>
  <div class="photo consult-photo" role="img" aria-label="Two colleagues reviewing work at a laptop"></div>
  <div class="futures-text">
    <h2>KORVEL FUTURES</h2>
    <p>Our Futures team turns research into products. Two machine learning systems grew from this work, each built to solve a real problem with clear, measurable results for the people using them.</p>
  </div>
  <div class="consult-label">KORVEL CONSULTANCY</div>
</section>

<section class="section product vigil">
  <div class="photo product-photo" role="img" aria-label="Driver's hands on a steering wheel"></div>
  <div class="product-text">
    <h2>VIGIL</h2>
    <p>The primary cause of accidents on the road is caused by human error. Of these, driver distraction and fatigue are the main problems.</p>
    <p>VIGIL is a system for every driver to make each journey safer, either for the driver and cabin or other road users.</p>
    <p>VIGIL uses advanced deep learning to monitor driver behaviour in real time. It can detect distraction such as phone usage, smoking or looking away from the road, and monitors for signs of fatigue.</p>
  </div>
</section>

<section class="section product pricewise">
  <div class="photo product-photo" role="img" aria-label="Business people signing a contract"></div>
  <div class="product-text">
    <h2>PRICEWISE</h2>
    <p>Pricewise is a machine learning system that tracks and analyses live used car trading markets. It takes every aspect of a car sale into account to create a powerful market intelligence for all parties in the used car ecosystem.</p>
    <p>It gives inexperienced buyers independent market consensus price, depreciation and approximate running costs for cars they are interested in.</p>
    <p>It provides dealerships comprehensive market intelligence including demands, supply, consensus price and expected market life of a car.</p>
  </div>
</section>

<section class="section expertise">
  <div class="photo" role="img" aria-label="Dark workspace with laptop and notes"></div>
  <div class="expertise-inner">
    <h2>STRONG EXPERTISE</h2>
    <p>We have many years of experience in machine learning, data mining, app development, DevOps and hardware design.</p>
    <p>We solve "hard" problems for business.</p>
  </div>
</section>

<section class="section help">
  <div class="photo help-photo" role="img" aria-label="Businessman in a suit standing in front of a rising blue growth arrow"></div>
  <h2>HOW WE CAN HELP</h2>
  <div class="help-list">
    <div class="help-item">
      <div class="help-icon"><svg width="36" height="36" viewBox="0 0 24 24"><path fill="#fff" d="M12 2c4 2 6 6 6 10l-3 3H9l-3-3c0-4 2-8 6-10zm0 6a2 2 0 1 0 0 4 2 2 0 0 0 0-4zM9 17h6l-3 5z"/></svg></div>
      <div><h3>Acquire more development capacity and get result fast</h3><p>Skilled people join your team quickly, so work moves on without delay.</p></div>
    </div>
    <div class="help-item">
      <div class="help-icon"><svg width="36" height="36" viewBox="0 0 24 24"><circle cx="12" cy="12" r="9" fill="none" stroke="#fff" stroke-width="2"/><text x="12" y="16.5" text-anchor="middle" font-size="12" font-family="Montserrat,sans-serif" font-weight="700" fill="#fff">$</text></svg></div>
      <div><h3>Avoid the overhead incurred by frequent scaling of your development team</h3></div>
    </div>
    <div class="help-item">
      <div class="help-icon"><svg width="36" height="36" viewBox="0 0 24 24"><circle cx="12" cy="12" r="9" fill="none" stroke="#fff" stroke-width="2"/><path d="M7 12l3.5 3.5L17 9" fill="none" stroke="#fff" stroke-width="2.4"/></svg></div>
      <div><h3>Reach a wide spectrum of expertise</h3></div>
    </div>
  </div>
</section>

<section class="section contact">
  <div class="photo" role="img" aria-label="Laptop and notebook on a dark desk"></div>
  <div class="contact-inner">
    <h2>CONTACT US</h2>
    <p class="intro">Thank you for your interest in Korvel services. We are glad you stopped by. For additional information regarding our audit and professional services offerings, please fill out the contact form and we will contact you promptly.</p>
    <div class="form">
      <div class="fields">
        <div class="field">Name</div>
        <div class="field">E-Mail</div>
        <div class="field">Phone</div>
      </div>
      <div class="field message">Message</div>
      <div class="submit">SUBMIT</div>
    </div>
  </div>
</section>

<footer class="section site-footer">
  <div class="footer-col">
    <h3>BLOG</h3>
    <div class="post"><div class="post-thumb" role="img" aria-label="Blog post thumbnail"></div><div><p>New release notes for our driver safety system are now online</p><span>Today 9:00 am - 12.05.2024</span></div></div>
    <div class="post"><div class="post-thumb" role="img" aria-label="Blog post thumbnail"></div><div><p>How used car markets change with live price data and trends</p><span>Today 2:30 pm - 10.05.2024</span></div></div>
  </div>
  <div class="footer-brand">
    <div class="brand"><span class="brand-dot"></span>KORVEL</div>
    <small>© KORVEL - 2024. All Rights Reserved</small>
  </div>
  <div class="footer-col info">
    <h3>CONTACT INFO</h3>
    <ul>
      <li><svg viewBox="0 0 24 24"><path fill="#1c8fd6" d="M12 2a7 7 0 0 0-7 7c0 5 7 13 7 13s7-8 7-13a7 7 0 0 0-7-7zm0 9.5A2.5 2.5 0 1 1 12 6.5a2.5 2.5 0 0 1 0 5z"/></svg>PO Box 88, Harbour Lane, Northgate, 4010</li>
      <li><svg viewBox="0 0 24 24"><path fill="#1c8fd6" d="M6.6 10.8a15 15 0 0 0 6.6 6.6l2.2-2.2c.3-.3.7-.4 1-.2 1.1.4 2.3.6 3.6.6.6 0 1 .4 1 1V20c0 .6-.4 1-1 1A17 17 0 0 1 3 4c0-.6.4-1 1-1h3.5c.6 0 1 .4 1 1 0 1.3.2 2.5.6 3.6.1.3 0 .7-.2 1z"/></svg>+61 400 555 010</li>
      <li><svg viewBox="0 0 24 24"><path fill="#1c8fd6" d="M2 5h20v14H2zm2 2v.5l8 5 8-5V7z"/></svg>hello@korvel.example</li>
    </ul>
  </div>
</footer>

</body>
</html>
```